KMW Plumbing and Roofing

design a fresh modern card for a young plumbing business looking to break into the market.
Must include the logo in the attached file
Bryce Olmo Verity
Phone number 0413962840
Vic Licence no 63194
email......

New Homes & Renovations
General Plumbing & Maintenance
Solar Hot Water Units
Roofing & Guttering (new and replacement)

Industry/Entity Type

Business

```html
<!DOCTYPE html>
<html lang="en">
<head>
<meta charset="utf-8">
<title>KMW Plumbing and Roofing – Business Card</title>
<link rel="stylesheet" href="https://fonts.googleapis.com/css2?family=Questrial&display=swap">
<style>
  :root {
    --page: #e8e6e2;
    --card: #ffffff;
    --brand-blue: #0b63c8;
    --navy: #133a6b;
    --ink: #1a1a1a;
    --white: #ffffff;
  }
  * { margin: 0; padding: 0; box-sizing: border-box; }
  html, body {
    width: 1200px; height: 900px; overflow: hidden;
    background: var(--page);
    font-family: "Questrial", "Century Gothic", sans-serif;
  }
  .canvas { position: relative; width: 1200px; height: 900px; }
  .card {
    position: absolute; top: 140px; width: 364px; height: 620px;
    border-radius: 14px; overflow: hidden;
  }
  .card--front { left: 219px; background: var(--card); }
  .card--back { left: 617px; background: var(--brand-blue); }

  .brand { position: absolute; display: flex; align-items: center; gap: 10px; }
  .brand__dot { width: 34px; height: 34px; border-radius: 50%; flex: none; }
  .brand__name { font-size: 17px; line-height: 1.15; }
  .card--front .brand { left: 64px; top: 82px; }
  .card--front .brand__dot { background: var(--navy); }
  .card--front .brand__name { color: var(--navy); }
  .card--back .brand { left: 26px; top: 494px; }
  .card--back .brand__dot { background: var(--white); width: 44px; height: 44px; }
  .card--back .brand__name { color: var(--white); font-size: 22px; }

  .contact {
    position: absolute; top: 268px; left: 0; width: 100%;
    text-align: center; color: var(--ink); font-size: 15px; line-height: 20px;
  }
  .contact__name { margin-bottom: 20px; }

  .services {
    position: absolute; left: 77px; width: 210px; top: 505px;
    color: var(--ink); font-size: 11.5px; line-height: 17px;
  }
  .services li {
    list-style: none; text-align: justify; text-align-last: justify;
    letter-spacing: 0.12em;
  }
  .services li.services__wide { letter-spacing: 0.02em; }

  .licence {
    position: absolute; left: 0; bottom: 0; width: 100%; height: 44px;
    background: var(--brand-blue); color: var(--ink);
    font-size: 17px; display: flex; align-items: center; justify-content: center;
  }
</style>
</head>
<body>
<main class="canvas">
  <section class="card card--front">
    <div class="brand">
      <span class="brand__dot"></span>
      <span class="brand__name">KMW Plumbing<br>and Roofing</span>
    </div>
    <div class="contact">
      <p class="contact__name">Bryce Olmo Verity</p>
      <p>T: 0413962840</p>
      <p>E: info@kmwplumbing.com</p>
    </div>
    <ul class="services">
      <li>New Homes &amp; Renovations</li>
      <li>Solar Hot Water Units</li>
      <li>Roofing &amp; Guttering</li>
      <li class="services__wide">General Plumbing &amp; Maintenance</li>
    </ul>
    <div class="licence">Vic Licence No: 63194</div>
  </section>

  <section class="card card--back">
    <div class="brand">
      <span class="brand__dot"></span>
      <span class="brand__name">KMW Plumbing<br>and Roofing</span>
    </div>
  </section>
</main>
</body>
</html>
```